Redesign of existing Web Design Project

I wish to redsesign the web pages on www.qbrl.com.au

Background of Harlowe Bexley

Harlowe Bexley Construction Services was established in 2004 as a boutique construction company offering construction advice and management services. We assist people in the construction minefield – step by step.

We offer services in: -

• Construction Management
• Project Management
• Building

The essence of our business is ensuring every project we undertake achieves the client’s objectives. Our experience has shown the secrets to a profitable project are -

• Planning
• Attention to detail
• Value add

We take the trouble to understand the client’s needs in person. Our hands-on approach ensures those involved deliver to the required quality standards at the scheduled times.

Our area of works include: -

• Residential single and multistorey developments
• Education facilities
• Suburban commercial building and refurbishment
• Health
• Defence
• Industrial

Objective of Acquisition

We are planning to expand our business activities. We are aiming to increase our turnover and use website as an increased passive selling tool.

Possible company type

This is an ideal opportunity for person who can capture readers attention.

Target Market(s)

see www.qbrl.com.au

Industry/Entity Type

Construction

Requirements
Must have
• Capture peoples attention on readers zones

```html
<!DOCTYPE html>
<html lang="en">
<head>
<meta charset="utf-8">
<title>Harlowe Bexley Construction Services</title>
<link href="https://fonts.googleapis.com/css2?family=Arimo:wght@400;700&family=Roboto+Condensed:wght@400;700&display=swap" rel="stylesheet">
<style>
:root{
  --page:#eaecee;
  --brand:#34506f;
  --teal:#2f6070;
  --nav-dark:#1f2e36;
  --nav-text:#4b5963;
  --overlay:rgba(4,40,55,.86);
  --card-border:#cfd2d5;
  --heading:#2a3a40;
  --body-text:#5b6468;
  --footer-text:#6a7176;
  --footer-link:#0e2f43;
}
*{box-sizing:border-box;margin:0;padding:0}
html,body{width:1200px;height:1052px;overflow:hidden}
body{background:var(--page);font-family:"Arimo",Arial,sans-serif;position:relative}

.brand{position:absolute;left:159px;top:58px;display:flex;align-items:center;gap:14px}
.brand-mark{width:46px;height:46px;background:var(--brand)}
.brand-name{font-family:"Arimo",Arial,sans-serif;font-weight:700;color:var(--brand);font-size:34px;line-height:1.05;letter-spacing:.2px}

.main-nav{position:absolute;left:159px;top:150px;width:882px;height:45px;
  border-top:4px solid var(--nav-dark);
  background:linear-gradient(#f2f4f6,#d9e0e6);border-bottom:1px solid #fff}
.main-nav::before{content:"";position:absolute;left:0;top:-4px;width:77px;height:4px;background:#8d9aa2}
.main-nav ul{list-style:none;display:flex;height:100%;padding-top:4px}
.main-nav li{font-size:13px;color:var(--nav-text);line-height:37px;padding:0 22px}
.main-nav li.current{background:var(--teal);color:#fff;width:76px;text-align:center;padding:0;margin-left:1px}
.search{position:absolute;right:9px;top:9px;width:210px;height:22px;background:#fff;border:1px solid #c3cad0;
  font-size:11px;font-style:italic;color:#9aa2a8;line-height:20px;padding-left:8px}
.search svg{position:absolute;right:3px;top:2px}

.hero{position:absolute;left:157px;top:206px;width:887px;height:375px;
  background:linear-gradient(180deg,#b9c6cf 0%,#8f9ea8 45%,#7d8a92 70%,#a4a9ac 100%)}
.hero-copy{position:absolute;left:27px;top:146px;width:400px;height:192px;background:var(--overlay);color:#fff;padding:8px 18px 0 10px}
.hero-copy h1{font-family:"Roboto Condensed","Arial Narrow",sans-serif;font-weight:400;font-size:32px;line-height:36px;padding-left:2px}
.hero-copy p{font-size:11.5px;line-height:17px;text-align:justify;margin-top:16px}
.hero-copy .more{position:absolute;right:23px;bottom:20px;font-size:11.5px;color:#8fa3ad}
.hero-edge{position:absolute;left:0;top:548px}

.services{position:absolute;left:159px;top:617px;display:flex;gap:18px}
.service{width:282px;height:272px;border:1px solid var(--card-border);background:linear-gradient(#fafafa,#eef0f1);padding:7px}
.service-photo{height:126px;border:1px solid #8b9093}
.service h2{font-family:"Roboto Condensed","Arial Narrow",sans-serif;font-weight:400;font-size:21px;color:var(--heading);margin:9px 0 8px -1px;letter-spacing:-.3px}
.service p{font-size:11.5px;line-height:17px;color:var(--body-text);text-align:justify;padding:0 9px 0 2px}

.site-footer{position:absolute;left:159px;top:938px;width:882px;border-top:1px solid #7d8488;text-align:center;font-size:11.5px;color:var(--footer-text);padding-top:25px;line-height:18px}
.site-footer .owner{color:var(--footer-link)}
</style>
</head>
<body>

<header class="brand">
  <div class="brand-mark"></div>
  <div class="brand-name">Harlowe Bexley<br>Construction Services</div>
</header>

<nav class="main-nav">
  <ul>
    <li class="current">Home</li>
    <li>About Us</li>
    <li>Links</li>
    <li>Free Downloads</li>
    <li>Careers</li>
    <li>Contacts</li>
  </ul>
  <div class="search">Type search here ...
    <svg width="18" height="16" viewBox="0 0 18 16"><circle cx="6.5" cy="6.5" r="4.5" fill="none" stroke="#3d4a52" stroke-width="2"/><line x1="10" y1="10" x2="16" y2="14" stroke="#3d4a52" stroke-width="3" stroke-linecap="round"/></svg>
  </div>
</nav>

<section class="hero" role="img" aria-label="Modern glass office building at dusk with a paved plaza">
  <div class="hero-copy">
    <h1>Deliver the project you want<br>on time, to budget</h1>
    <p>The essence of our business is ensuring every project we undertake achieves the client’s objectives. Our experience has shown the secrets to a profitable project are PLANNING, &nbsp;ATTENTION TO DETAIL, VALUE ADD</p>
    <span class="more">+ Read more</span>
  </div>
</section>
<svg class="hero-edge" width="1200" height="60" viewBox="0 0 1200 60">
  <defs><linearGradient id="edgeShade" x1="0" y1="0" x2="0" y2="1"><stop offset="0" stop-color="#d6d9dc"/><stop offset="1" stop-color="#eaecee"/></linearGradient></defs>
  <path d="M0 52 C300 36 420 11 600 10 C780 11 900 36 1200 52 L1200 60 L0 60 Z" fill="url(#edgeShade)"/>
</svg>

<main class="services">
  <article class="service">
    <div class="service-photo" role="img" aria-label="Hands reviewing building plans with a hard hat" style="background:linear-gradient(135deg,#5e7ea8,#c9d3e0 55%,#e7b84a)"></div>
    <h2>Construction Management</h2>
    <p>From start to finish; from demolition and site excavation to lock up, council sign off and tax depreciation. Our Project Management process is a detailed....</p>
  </article>
  <article class="service">
    <div class="service-photo" role="img" aria-label="Two managers in hard hats on a construction site" style="background:linear-gradient(135deg,#8a6a4e,#c7c2b8 50%,#3a4e9a)"></div>
    <h2>Project Management</h2>
    <p>From start to finish; from demolition and site excavation to lock up, council sign off and tax depreciation. Our Project Management process is a detailed....</p>
  </article>
  <article class="service">
    <div class="service-photo" role="img" aria-label="Crane lifting a load against a blue sky" style="background:linear-gradient(160deg,#3b4a5c,#6f9dd2 40%,#a9c7e6)"></div>
    <h2>Building</h2>
    <p>From start to finish; from demolition and site excavation to lock up, council sign off and tax depreciation. Our Project Management process is a detailed....</p>
  </article>
</main>

<footer class="site-footer">
  Home | About Us | Building | Construction Management | Project Management | Links | Free Downloads | Careers | Contacts<br>
  Copyright © 2008 <span class="owner">Harlowe Bexley</span>, All Rights Reserved - Webmaster &nbsp;&nbsp;&nbsp;| &nbsp;&nbsp;&nbsp;Privacy policy &nbsp;&nbsp;&nbsp;| &nbsp;&nbsp;&nbsp;Admint
</footer>

</body>
</html>
```